Power point for Phd defence - surgical science

Create a powerpoint for my Phd thesis defence at Brellmoor University. It's scientific presentation of 4 trials I have conducted. 40 minutes, approx. 50 slides. Should consist of 1. Welcome, 2. Background, 3. Presentation of study 1-4 (methods, results, limitations), 4. Discussion, 5. Perspectives, 6. Conclusions
I'd like a nice template where I can add the scientific content which can later be revised.
Deadline November 6.

Target Market(s)

Medical doctors / Surgeons / Professors / Family

Industry/Entity Type

Surgery

Colors

Designer to choose only greyscale colors for use in the design.

Requirements
Must have
• Brellmoor university logo
Nice to have
• I want a nice balance between scientific content and information that can be understood by my family and friends. I'd it to be professional but still light and easy to follow.

```html
<!DOCTYPE html>
<html lang="en">
<head>
<meta charset="utf-8">
<title>PhD Defence – Surgical Science Slide Template</title>
<link href="https://fonts.googleapis.com/css2?family=Open+Sans:wght@400;600;700&display=swap" rel="stylesheet">
<style>
:root{
  --canvas:#f3f3f5;
  --paper:#ffffff;
  --accent:#3a3a3f;
  --accent-dark:#1f1f22;
  --accent-light:#5c5c63;
  --accent-mid:#8a8a91;
  --tint:#d9d9dd;
  --tint-soft:#ececef;
  --ink:#26262b;
  --muted:#8d8d94;
  --line:#dcdce0;
}
*{box-sizing:border-box;margin:0;padding:0}
html,body{width:1200px;height:3374px;overflow:hidden}
body{background:var(--canvas);font-family:"Open Sans",Arial,sans-serif;color:var(--ink);position:relative}
.slide{position:absolute;width:464px;height:261px;background:var(--paper);box-shadow:0 8px 22px rgba(0,0,0,.08);overflow:hidden}
.slide.dark{background:linear-gradient(120deg,var(--accent-dark),var(--accent) 55%,var(--accent-light));color:#fff}
.col-l{left:102px}.col-r{left:634px}
.abs{position:absolute}
.eyebrow{position:absolute;left:26px;top:16px;font-size:5.5px;color:var(--accent-mid)}
.slide.dark .eyebrow{color:#cfcfd3}
.title{position:absolute;left:26px;top:24px;font-size:11px;font-weight:700}
.brand{position:absolute;right:24px;top:16px;display:flex;align-items:center;gap:4px}
.brand-dot{width:10px;height:10px;border-radius:50%;background:var(--accent)}
.slide.dark .brand-dot{background:#fff}
.brand-name{font-size:4.6px;font-weight:600;letter-spacing:.6px;line-height:1.1;color:var(--muted);text-transform:uppercase}
.slide.dark .brand-name{color:#fff}
.brand-rule{position:absolute;right:24px;top:33px;width:72px;height:1px;background:var(--line)}
.slide.dark .brand-rule{background:rgba(255,255,255,.4)}
.url{position:absolute;left:24px;bottom:12px;font-size:5px;color:var(--muted)}
.page{position:absolute;right:24px;bottom:12px;font-size:5px;color:var(--muted)}
.page b{color:var(--accent);font-weight:600}
.slide.dark .url,.slide.dark .page,.slide.dark .page b{color:#fff}
.photo{position:absolute;background:linear-gradient(145deg,#d8d8dc,#9c9ca3)}
.photo.deep{background:linear-gradient(135deg,#6a6a70,#2e2e33)}
.photo.night{background:linear-gradient(135deg,#4a4a50,#1c1c20)}
.photo.slate{background:linear-gradient(135deg,#707077,#33333a)}
.tiny{font-size:4px;line-height:1.5;color:var(--muted)}
.label{font-size:5px;font-weight:700;color:var(--ink)}
.card{position:absolute;background:#fff;box-shadow:0 3px 10px rgba(0,0,0,.12)}
.card.darkcard{background:linear-gradient(135deg,var(--accent-light),var(--accent-dark));color:#fff}
.center{text-align:center}
.toc-row{position:absolute;width:160px;height:12px;border-bottom:1px solid var(--line);font-size:4.5px;font-weight:700;display:flex;justify-content:space-between;align-items:flex-end;padding-bottom:2px}
.stat{position:absolute;width:42px;height:48px;background:#fff;box-shadow:0 3px 10px rgba(0,0,0,.12);text-align:center;padding-top:14px}
.stat b{display:block;font-size:8px}
.stat span{font-size:4px;color:var(--muted)}
.stat.hi{background:var(--accent);color:#fff;height:50px;top:-2px}
.stat.hi span{color:#fff}
.method{position:absolute;width:90px;text-align:center}
.method svg{display:block;margin:0 auto 4px}
.ring-badge{position:absolute;width:26px;height:26px;border-radius:50%;background:#fff;border:2px solid var(--accent);box-shadow:0 2px 6px rgba(0,0,0,.2);font-size:5px;font-weight:700;display:flex;align-items:center;justify-content:center}
.tile{position:absolute;width:84px;height:90px;background:rgba(255,255,255,.08);text-align:center;padding-top:18px}
.tile .label{color:#fff;margin-top:8px}
.big{font-size:14px;font-weight:400;color:var(--accent)}
.accent-text{color:var(--accent)}
.bar-track{position:absolute;height:6px;border-radius:3px;background:#fff;box-shadow:0 2px 6px rgba(0,0,0,.12)}
.bar-fill{height:3px;margin:1.5px 4px;background:var(--accent);border-radius:2px}
/* svg paint helpers */
.fa{fill:var(--accent)}.fad{fill:var(--accent-dark)}.fal{fill:var(--accent-light)}.fam{fill:var(--accent-mid)}
.ft{fill:var(--tint)}.fts{fill:var(--tint-soft)}.fw{fill:#fff}.fi{fill:var(--ink)}.fm{fill:var(--muted)}
.sa{stroke:var(--accent)}.st{stroke:var(--tint)}.sl{stroke:#c9c9cf}.sw{stroke:#fff}.sm{stroke:#555}
.nf{fill:none}
</style>
</head>
<body>

<!-- 1 Cover -->
<section class="slide dark col-l" style="top:109px">
  <div class="photo" style="left:220px;top:0;width:244px;height:261px;background:linear-gradient(90deg,rgba(58,58,63,0),#dcdcdf 45%,#efeff1)" role="img" aria-label="Portrait photo of a surgeon wearing a face mask and white coat"></div>
  <div class="abs" style="left:36px;top:56px;display:flex;align-items:center;gap:5px">
    <div style="width:22px;height:22px;border-radius:50%;background:#fff"></div>
    <div style="font-size:6px;font-weight:600;color:#fff">Brellmoor University</div>
  </div>
  <div class="abs" style="left:34px;top:132px;font-size:23px;font-weight:700">Phd Defence</div>
  <div class="abs" style="left:35px;top:164px;font-size:5.5px;font-weight:600">Brellmoor University</div>
  <div class="abs" style="left:35px;top:232px;font-size:5px">www.brellmoor.edu/english/</div>
</section>

<!-- 2 Title -->
<section class="slide dark col-r" style="top:109px">
  <div class="abs" style="left:0;width:464px;top:38px;display:flex;flex-direction:column;align-items:center;gap:3px">
    <div style="width:20px;height:20px;border-radius:50%;background:#fff"></div>
    <div style="font-size:5px;font-weight:600">Brellmoor University</div>
  </div>
  <div class="abs center" style="left:0;width:464px;top:104px;font-size:22px;font-weight:700">Phd Defence</div>
  <div class="abs center" style="left:0;width:464px;top:133px;font-size:9px">Surgical Science</div>
  <div class="abs" style="left:160px;top:193px;font-size:5.5px;font-weight:600">Mr. Aron Vessby</div>
  <div class="abs" style="left:253px;top:193px;font-size:5.5px;font-weight:600">October 2023</div>
  <div class="abs center" style="left:0;width:464px;top:224px;font-size:5px">www.brellmoor.edu/english/</div>
</section>

<!-- 3 Presentation List -->
<section class="slide col-l" style="top:432px">
  <div class="eyebrow">Collage University</div><div class="title">Presentation List</div>
  <div class="brand"><div class="brand-dot"></div><div class="brand-name">Brellmoor<br>University</div></div><div class="brand-rule"></div>
  <div class="toc-row" style="left:54px;top:66px"><span>COVER SLIDES</span><span>01</span></div>
  <div class="toc-row" style="left:54px;top:102px"><span>PRESENTATION LIST</span><span>02</span></div>
  <div class="toc-row" style="left:54px;top:138px"><span>THESIS OVERVIEW</span><span>03</span></div>
  <div class="toc-row" style="left:54px;top:174px"><span>PATENTED PRODUCTS</span><span>04</span></div>
  <div class="toc-row" style="left:252px;top:66px"><span>TECHNOLOGY SUMMARY</span><span>05</span></div>
  <div class="toc-row" style="left:252px;top:102px"><span>RESEARCH ANALYSE</span><span>06</span></div>
  <div class="toc-row" style="left:252px;top:138px"><span>RESEARCH ANALYSE II</span><span>07</span></div>
  <div class="toc-row" style="left:252px;top:174px"><span>CLOSING SLIDE</span><span>08</span></div>
  <div class="url">www.brellmoor.edu/english/</div><div class="page">Page | <b>3</b></div>
</section>

<!-- 4 Surgical Science -->
<section class="slide col-r" style="top:432px">
  <div class="eyebrow">Collage University</div><div class="title">Surgical Science</div>
  <div class="brand"><div class="brand-dot"></div><div class="brand-name">Brellmoor<br>University</div></div><div class="brand-rule"></div>
  <div class="photo deep" style="left:44px;top:66px;width:98px;height:135px" role="img" aria-label="Photo of a masked surgeon"></div>
  <div class="abs tiny" style="left:208px;top:66px;width:210px">Lorem ipsum dolor sit amet, consectetur adipiscing elit. Maecenas porttitor congue massa. Fusce posuere, magna sed pulvinar ultricies, purus lectus malesuada libero, sit amet commodo magna eros quis urna.<br><br>Nunc viverra imperdiet enim. Fusce est. Vivamus a tellus. Pellentesque habitant morbi tristique senectus et netus et malesuada fames ac turpis egestas. Proin pharetra nonummy pede. Mauris et orci.</div>
  <div class="abs" style="left:208px;top:154px;width:140px;height:48px">
    <div class="stat" style="left:0"><b>12+</b><span>Experiments</span></div>
    <div class="stat hi" style="left:46px"><b>400+</b><span>Participant</span></div>
    <div class="stat" style="left:92px"><b>8</b><span>Partners</span></div>
  </div>
  <div class="url">www.brellmoor.edu/english/</div><div class="page">Page | <b>4</b></div>
</section>

<!-- 5 Background -->
<section class="slide col-l" style="top:754px">
  <div class="eyebrow">Collage University</div><div class="title">Background of Research</div>
  <div class="brand"><div class="brand-dot"></div><div class="brand-name">Brellmoor<br>University</div></div><div class="brand-rule"></div>
  <div class="photo" style="left:28px;top:64px;width:86px;height:108px;background:linear-gradient(160deg,#eaeaec,#bfbfc4)" role="img" aria-label="Photo of gloved hands raised"></div>
  <div class="photo" style="left:124px;top:106px;width:86px;height:108px;background:linear-gradient(140deg,#7e7e83,#38383c)" role="img" aria-label="Top view of surgeons around an operating table"></div>
  <svg class="abs" style="left:252px;top:66px" width="14" height="120"><line x1="7" y1="4" x2="7" y2="82" class="st" stroke-width="1"/><circle cx="7" cy="5" r="5" class="fa"/><circle cx="7" cy="78" r="5" class="fa"/></svg>
  <div class="abs" style="left:270px;top:67px;width:160px"><div class="label">Section One</div><div class="tiny" style="margin-top:3px">• Lorem ipsum dolor sit amet, consectetur adipiscing elit. Maecenas porttitor congue massa.<br>• Lorem ipsum dolor sit amet, consectetur adipiscing elit. Maecenas porttitor congue massa.<br>• Lorem ipsum dolor sit amet, consectetur adipiscing elit.</div></div>
  <div class="abs" style="left:270px;top:140px;width:160px"><div class="label">Section Two</div><div class="tiny" style="margin-top:3px">• Lorem ipsum dolor sit amet, consectetur adipiscing elit. Maecenas porttitor congue massa.<br>• Lorem ipsum dolor sit amet, consectetur adipiscing elit. Maecenas porttitor congue massa.<br>• Lorem ipsum dolor sit amet, consectetur adipiscing elit.</div></div>
  <div class="url">www.brellmoor.edu/english/</div><div class="page">Page | <b>5</b></div>
</section>

<!-- 6 Methods -->
<section class="slide col-r" style="top:754px">
  <div class="eyebrow">Collage University</div><div class="title">Methods</div>
  <div class="brand"><div class="brand-dot"></div><div class="brand-name">Brellmoor<br>University</div></div><div class="brand-rule"></div>
  <div class="method" style="left:56px;top:68px"><svg width="14" height="14"><rect x="2" y="2" width="10" height="8" class="nf sm"/><line x1="4" y1="13" x2="10" y2="13" class="sm"/></svg><div class="label">Method One</div><div class="tiny">Lorem ipsum dolor sit amet, consectetur adipiscing elit. Maecenas porttitor congue massa. Fusce posuere.</div></div>
  <div class="method" style="left:186px;top:68px"><svg width="14" height="14"><rect x="2" y="1" width="10" height="12" class="nf sm"/><line x1="4" y1="5" x2="10" y2="5" class="sm"/><line x1="4" y1="8" x2="10" y2="8" class="sm"/></svg><div class="label">Method Two</div><div class="tiny">Lorem ipsum dolor sit amet, consectetur adipiscing elit. Maecenas porttitor congue massa. Fusce posuere.</div></div>
  <div class="method" style="left:316px;top:68px"><svg width="14" height="14"><path d="M3 2h8v4a4 4 0 0 1-8 0z" class="nf sm"/><line x1="7" y1="10" x2="7" y2="13" class="sm"/></svg><div class="label">Method Three</div><div class="tiny">Lorem ipsum dolor sit amet, consectetur adipiscing elit. Maecenas porttitor congue massa. Fusce posuere.</div></div>
  <div class="method" style="left:56px;top:158px"><svg width="14" height="14"><circle cx="7" cy="6" r="4.5" class="nf sm"/><path d="M4 10l-1 3h8l-1-3" class="nf sm"/></svg><div class="label">Method Four</div><div class="tiny">Lorem ipsum dolor sit amet, consectetur adipiscing elit. Maecenas porttitor congue massa. Fusce posuere.</div></div>
  <div class="method" style="left:186px;top:158px"><svg width="14" height="14"><rect x="3" y="2" width="8" height="11" class="nf sm"/><rect x="5" y="1" width="4" height="2" style="fill:#555"/></svg><div class="label">Method Five</div><div class="tiny">Lorem ipsum dolor sit amet, consectetur adipiscing elit. Maecenas porttitor congue massa. Fusce posuere.</div></div>
  <div class="method" style="left:316px;top:158px"><svg width="14" height="14"><path d="M5 1h4M6 1v5l-4 7h10l-4-7V1" class="nf sm"/></svg><div class="label">Method Six</div><div class="tiny">Lorem ipsum dolor sit amet, consectetur adipiscing elit. Maecenas porttitor congue massa. Fusce posuere.</div></div>
  <div class="url">www.brellmoor.edu/english/</div><div class="page">Page | <b>6</b></div>
</section>

<!-- 7 Analyse with Pictures -->
<section class="slide col-l" style="top:1077px">
  <div class="eyebrow">Collage University</div><div class="title">Analyse with Pictures</div>
  <div class="brand"><div class="brand-dot"></div><div class="brand-name">Brellmoor<br>University</div></div><div class="brand-rule"></div>
  <div class="photo night" style="left:48px;top:58px;width:110px;height:94px" role="img" aria-label="Microscope image of cells"></div>
  <div class="photo" style="left:177px;top:58px;width:110px;height:94px;background:linear-gradient(160deg,#eaeaec,#bfbfc4)" role="img" aria-label="Photo of gloved hands"></div>
  <div class="photo slate" style="left:306px;top:58px;width:110px;height:94px" role="img" aria-label="Photo of a surgeon in theatre"></div>
  <div class="ring-badge" style="left:90px;top:138px">40%</div>
  <div class="ring-badge" style="left:219px;top:138px">60%</div>
  <div class="ring-badge" style="left:348px;top:138px">80%</div>
  <div class="abs center" style="left:48px;top:170px;width:110px"><div class="label" style="font-size:4.5px">Analyse <span class="accent-text" style="font-weight:400">One</span></div><div class="tiny">Lorem ipsum dolor sit amet, consectetur adipiscing elit. Maecenas porttitor congue massa. Fusce posuere.</div></div>
  <div class="abs center" style="left:177px;top:170px;width:110px"><div class="label" style="font-size:4.5px">Analyse <span class="accent-text" style="font-weight:400">Two</span></div><div class="tiny">Lorem ipsum dolor sit amet, consectetur adipiscing elit. Maecenas porttitor congue massa. Fusce posuere.</div></div>
  <div class="abs center" style="left:306px;top:170px;width:110px"><div class="label" style="font-size:4.5px">Analyse <span class="accent-text" style="font-weight:400">Three</span></div><div class="tiny">Lorem ipsum dolor sit amet, consectetur adipiscing elit. Maecenas porttitor congue massa. Fusce posuere.</div></div>
  <div class="url">www.brellmoor.edu/english/</div><div class="page">Page | <b>7</b></div>
</section>

<!-- 8 Analyse with Icons -->
<section class="slide dark col-r" style="top:1077px">
  <div class="eyebrow">Collage University</div><div class="title">Analyse with Icons</div>
  <div class="brand"><div class="brand-dot"></div><div class="brand-name">Brellmoor<br>University</div></div><div class="brand-rule"></div>
  <div class="tile" style="left:34px;top:74px"><svg width="24" height="24"><rect x="5" y="3" width="14" height="19" class="nf sw"/><line x1="8" y1="9" x2="16" y2="9" class="sw"/><line x1="8" y1="13" x2="16" y2="13" class="sw"/><line x1="8" y1="17" x2="13" y2="17" class="sw"/></svg><div class="label">Section One</div></div>
  <div class="tile" style="left:138px;top:74px"><svg width="24" height="24"><circle cx="12" cy="12" r="8" class="nf sw" stroke-dasharray="3 2"/><circle cx="12" cy="12" r="4" class="nf sw"/></svg><div class="label">Section Two</div></div>
  <div class="tile" style="left:242px;top:74px"><svg width="24" height="24"><rect x="3" y="12" width="8" height="8" class="nf sw"/><rect x="13" y="12" width="8" height="8" class="nf sw"/><rect x="8" y="3" width="8" height="8" class="nf sw"/></svg><div class="label">Section Three</div></div>
  <div class="tile" style="left:346px;top:74px"><svg width="24" height="24"><circle cx="12" cy="12" r="3" class="nf sw"/><circle cx="4" cy="6" r="2" class="nf sw"/><circle cx="20" cy="6" r="2" class="nf sw"/><circle cx="12" cy="21" r="2" class="nf sw"/><path d="M6 7l4 3M18 7l-4 3M12 15v4" class="sw"/></svg><div class="label">Section Four</div></div>
  <div class="abs tiny center" style="left:34px;top:170px;width:84px;color:#fff">Lorem ipsum dolor sit amet, consectetur adipiscing elit. Maecenas porttitor.</div>
  <div class="abs tiny center" style="left:138px;top:170px;width:84px;color:#fff">Lorem ipsum dolor sit amet, consectetur adipiscing elit. Maecenas porttitor.</div>
  <div class="abs tiny center" style="left:242px;top:170px;width:84px;color:#fff">Lorem ipsum dolor sit amet, consectetur adipiscing elit. Maecenas porttitor.</div>
  <div class="abs tiny center" style="left:346px;top:170px;width:84px;color:#fff">Lorem ipsum dolor sit amet, consectetur adipiscing elit. Maecenas porttitor.</div>
  <div class="url">www.brellmoor.edu/english/</div><div class="page">Page | <b>8</b></div>
</section>

<!-- 9 Section of Research -->
<section class="slide col-l" style="top:1399px">
  <div class="eyebrow">Collage University</div><div class="title">Section of Research</div>
  <div class="brand"><div class="brand-dot"></div><div class="brand-name">Brellmoor<br>University</div></div><div class="brand-rule"></div>
  <div class="card" style="left:124px;top:56px;width:100px;height:82px;padding:12px 10px"><div class="label accent-text">◎ &nbsp;Section One</div><div class="tiny" style="margin-top:8px">Lorem ipsum dolor sit amet, consectetuer adipisc. Maecenas porttitor congue.</div></div>
  <div class="card darkcard" style="left:232px;top:52px;width:100px;height:82px;padding:12px 10px"><div style="font-size:5px;font-weight:600">▦ &nbsp;Section Three</div><div style="font-size:6px;text-align:right;margin-top:14px">Increase/Years</div><div style="font-size:13px;text-align:right">+38%</div></div>
  <div class="card" style="left:124px;top:146px;width:100px;height:80px;padding:12px 10px"><div class="label accent-text">▤ &nbsp;Section Two</div><div style="font-size:6px;text-align:right;margin-top:14px;color:var(--muted)">Increase / Years</div><div class="big" style="text-align:right">43%</div></div>
  <div class="card" style="left:232px;top:146px;width:100px;height:80px;padding:12px 10px"><div class="label accent-text">◎ &nbsp;Section Four</div><div style="font-size:6px;text-align:right;margin-top:14px;color:var(--muted)">Loss / Years</div><div class="big" style="text-align:right">2.1%</div></div>
  <div class="url">www.brellmoor.edu/english/</div><div class="page">Page | <b>9</b></div>
</section>

<!-- 10 Research Timeline -->
<section class="slide col-r" style="top:1399px">
  <div class="eyebrow">Collage University</div><div class="title">Research Timeline</div>
  <div class="brand"><div class="brand-dot"></div><div class="brand-name">Brellmoor<br>University</div></div><div class="brand-rule"></div>
  <svg class="abs" style="left:0;top:0" width="464" height="261">
    <line x1="26" y1="134" x2="464" y2="134" class="sl"/>
    <g class="fw st"><circle cx="44" cy="113" r="8"/><circle cx="148" cy="154" r="7"/><circle cx="256" cy="113" r="10"/><circle cx="360" cy="154" r="7"/></g>
    <g class="fa"><circle cx="44" cy="134" r="1.5"/><circle cx="148" cy="134" r="1.5"/><circle cx="256" cy="134" r="1.5"/><circle cx="360" cy="134" r="1.5"/></g>
  </svg>
  <div class="abs tiny" style="left:40px;top:146px;width:80px"><b style="color:var(--ink)">March 2023</b><br>Lorem ipsum dolor sit amet, consectetuer adipisc. Maecenas porttitor congue.</div>
  <div class="abs tiny" style="left:146px;top:88px;width:80px"><b style="color:var(--ink)">April 2023</b><br>Lorem ipsum dolor sit amet, consectetuer adipisc. Maecenas porttitor congue.</div>
  <div class="abs tiny" style="left:254px;top:146px;width:80px"><b style="color:var(--ink)">May 2023</b><br>Lorem ipsum dolor sit amet, consectetuer adipisc. Maecenas porttitor congue.</div>
  <div class="abs tiny" style="left:358px;top:88px;width:80px"><b style="color:var(--ink)">June 2023</b><br>Lorem ipsum dolor sit amet, consectetuer adipisc. Maecenas porttitor congue.</div>
  <div class="url">www.brellmoor.edu/english/</div><div class="page">Page | <b>10</b></div>
</section>

<!-- 11 Research Timeline -->
<section class="slide col-l" style="top:1722px">
  <div class="eyebrow">Collage University</div><div class="title">Research Timeline</div>
  <div class="brand"><div class="brand-dot"></div><div class="brand-name">Brellmoor<br>University</div></div><div class="brand-rule"></div>
  <svg class="abs" style="left:0;top:0" width="464" height="261">
    <line x1="0" y1="134" x2="390" y2="134" class="sl"/>
    <circle cx="204" cy="100" r="16" class="fw st" stroke-width="3"/><circle cx="204" cy="100" r="12" class="fa"/>
    <rect x="198" y="96" width="12" height="8" class="nf sw"/>
    <circle cx="60" cy="153" r="7" class="fw st"/><circle cx="356" cy="153" r="7" class="fw st"/>
    <g class="fa"><circle cx="60" cy="134" r="1.5"/><circle cx="204" cy="134" r="1.5"/><circle cx="356" cy="134" r="1.5"/></g>
  </svg>
  <div class="abs tiny" style="left:58px;top:88px;width:80px"><b style="color:var(--ink)">July 2023</b><br>Lorem ipsum dolor sit amet, consectetuer adipisc. Maecenas porttitor congue.</div>
  <div class="abs tiny" style="left:202px;top:146px;width:80px"><b style="color:var(--ink)">August 2023</b><br>Lorem ipsum dolor sit amet, consectetuer adipisc. Maecenas porttitor congue.</div>
  <div class="abs tiny" style="left:354px;top:88px;width:80px"><b style="color:var(--ink)">September 2023</b><br>Lorem ipsum dolor sit amet, consectetuer adipisc. Maecenas porttitor congue.</div>
  <div class="url">www.brellmoor.edu/english/</div><div class="page">Page | <b>11</b></div>
</section>

<!-- 12 Research Timeline -->
<section class="slide col-r" style="top:1722px">
  <div class="eyebrow">Collage University</div><div class="title">Research Timeline</div>
  <div class="brand"><div class="brand-dot"></div><div class="brand-name">Brellmoor<br>University</div></div><div class="brand-rule"></div>
  <svg class="abs" style="left:0;top:0" width="464" height="261">
    <line x1="70" y1="134" x2="398" y2="134" class="sa" stroke-width="1.5"/>
    <g class="sa" stroke-dasharray="2 2"><line x1="70" y1="134" x2="70" y2="170"/><line x1="152" y1="134" x2="152" y2="92"/><line x1="234" y1="134" x2="234" y2="170"/><line x1="316" y1="134" x2="316" y2="92"/><line x1="398" y1="134" x2="398" y2="170"/></g>
    <g class="fa st" stroke-width="3"><circle cx="70" cy="134" r="10"/><circle cx="152" cy="134" r="10"/><circle cx="234" cy="134" r="10"/><circle cx="316" cy="134" r="10"/><circle cx="398" cy="134" r="10"/></g>
    <g class="nf sw"><rect x="66" y="130" width="8" height="8"/><circle cx="152" cy="134" r="4"/><rect x="230" y="130" width="8" height="8"/><circle cx="316" cy="134" r="4"/><rect x="394" y="130" width="8" height="8"/></g>
  </svg>
  <div class="abs tiny center" style="left:105px;top:60px;width:94px"><b style="color:var(--ink)">Section One</b><br>Lorem ipsum dolor sit amet, consectetuer adipiscing elit. Maecenas porttitor congue massa.</div>
  <div class="abs tiny center" style="left:269px;top:60px;width:94px"><b style="color:var(--ink)">Section One</b><br>Lorem ipsum dolor sit amet, consectetuer adipiscing elit. Maecenas porttitor congue massa.</div>
  <div class="abs tiny center" style="left:23px;top:172px;width:94px"><b style="color:var(--ink)">Section One</b><br>Lorem ipsum dolor sit amet, consectetuer adipiscing elit. Maecenas porttitor congue massa.</div>
  <div class="abs tiny center" style="left:187px;top:172px;width:94px"><b style="color:var(--ink)">Section One</b><br>Lorem ipsum dolor sit amet, consectetuer adipiscing elit. Maecenas porttitor congue massa.</div>
  <div class="abs tiny center" style="left:351px;top:172px;width:94px"><b style="color:var(--ink)">Section One</b><br>Lorem ipsum dolor sit amet, consectetuer adipiscing elit. Maecenas porttitor congue massa.</div>
  <div class="url">www.brellmoor.edu/english/</div><div class="page">Page | <b>12</b></div>
</section>

<!-- 13 Chart Analise -->
<section class="slide col-l" style="top:2045px">
  <div class="eyebrow">Collage University</div><div class="title">Chart Analise</div>
  <div class="brand"><div class="brand-dot"></div><div class="brand-name">Brellmoor<br>University</div></div><div class="brand-rule"></div>
  <svg class="abs" style="left:0;top:0" width="464" height="261" font-family="Open Sans, Arial, sans-serif">
    <rect x="308" y="64" width="3" height="3" class="fad"/><text x="313" y="67" font-size="4" class="fm">Region 1</text>
    <rect x="364" y="64" width="3" height="3" class="fam"/><text x="369" y="67" font-size="4" class="fm">Region 2</text>
    <g font-size="4" class="fm" text-anchor="end"><text x="44" y="102">125</text><text x="44" y="122">100</text><text x="44" y="142">75</text><text x="44" y="162">50</text><text x="44" y="182">25</text><text x="44" y="202">0</text></g>
    <line x1="48" y1="200" x2="410" y2="200" class="st"/>
    <g class="fad"><rect x="62" y="186" width="10" height="14"/><rect x="114" y="178" width="10" height="22"/><rect x="166" y="156" width="10" height="44"/><rect x="218" y="120" width="10" height="80"/><rect x="270" y="184" width="10" height="16"/><rect x="322" y="158" width="10" height="42"/><rect x="374" y="124" width="10" height="76"/></g>
    <g class="fam"><rect x="75" y="156" width="10" height="44"/><rect x="127" y="164" width="10" height="36"/><rect x="179" y="144" width="10" height="56"/><rect x="231" y="152" width="10" height="48"/><rect x="283" y="166" width="10" height="34"/><rect x="335" y="142" width="10" height="58"/><rect x="387" y="152" width="10" height="48"/></g>
    <g class="fa"><rect x="70" y="132" width="22" height="9"/><rect x="172" y="118" width="22" height="9"/><rect x="224" y="96" width="22" height="9"/><rect x="378" y="100" width="22" height="9"/></g>
    <g class="fw" font-size="3.5" text-anchor="middle"><text x="81" y="138">up 56%</text><text x="183" y="124">up 63%</text><text x="235" y="102">up 48%</text><text x="389" y="106">up 23%</text></g>
    <g font-size="4" class="fm" text-anchor="middle"><text x="73" y="210">April</text><text x="125" y="210">May</text><text x="177" y="210">June</text><text x="229" y="210">July</text><text x="281" y="210">May</text><text x="333" y="210">June</text><text x="385" y="210">July</text></g>
  </svg>
  <div class="url">www.brellmoor.edu/english/</div><div class="page">Page | <b>13</b></div>
</section>

<!-- 14 Dashboard -->
<section class="slide col-r" style="top:2045px">
  <div class="eyebrow">Collage University</div><div class="title">Dashboard Slide</div>
  <div class="brand"><div class="brand-dot"></div><div class="brand-name">Brellmoor<br>University</div></div><div class="brand-rule"></div>
  <div class="abs center" style="left:48px;top:62px;width:60px"><div class="accent-text" style="font-size:10px;font-weight:600">+$3M</div><div class="tiny">Yearly Profit</div></div>
  <div class="card center" style="left:144px;top:56px;width:80px;height:36px;padding-top:7px"><div class="accent-text" style="font-size:10px;font-weight:600">1281</div><div class="tiny">Projects Completed</div></div>
  <div class="abs center" style="left:250px;top:62px;width:60px"><div class="accent-text" style="font-size:10px;font-weight:600">10K</div><div class="tiny">Project Hours</div></div>
  <div class="abs center" style="left:350px;top:62px;width:60px"><div class="accent-text" style="font-size:10px;font-weight:600">14</div><div class="tiny">Certifications</div></div>
  <div class="card" style="left:34px;top:114px;width:282px;height:98px">
    <svg width="282" height="98" font-family="Open Sans, Arial, sans-serif">
      <defs><linearGradient id="barGrad" x1="0" y1="0" x2="0" y2="1"><stop offset="0" stop-color="#1f1f22"/><stop offset="1" stop-color="#9a9aa1"/></linearGradient></defs>
      <text x="8" y="11" font-size="4" font-weight="700" class="fi">Data Statistics</text>
      <g fill="url(#barGrad)"><rect x="20" y="40" width="6" height="44"/><rect x="41" y="30" width="6" height="54"/><rect x="62" y="26" width="6" height="58"/><rect x="83" y="34" width="6" height="50"/><rect x="104" y="40" width="6" height="44"/><rect x="125" y="36" width="6" height="48"/><rect x="146" y="44" width="6" height="40"/><rect x="167" y="38" width="6" height="46"/><rect x="188" y="40" width="6" height="44"/><rect x="209" y="28" width="6" height="56"/><rect x="230" y="34" width="6" height="50"/><rect x="251" y="24" width="6" height="60"/></g>
      <g font-size="4" class="fm" text-anchor="middle"><text x="23" y="92">1</text><text x="44" y="92">2</text><text x="65" y="92">3</text><text x="86" y="92">4</text><text x="107" y="92">5</text><text x="128" y="92">6</text><text x="149" y="92">7</text><text x="170" y="92">8</text><text x="191" y="92">9</text><text x="212" y="92">10</text><text x="233" y="92">11</text><text x="254" y="92">12</text></g>
    </svg>
  </div>
  <div class="card" style="left:326px;top:114px;width:104px;height:98px">
    <svg width="104" height="98" font-family="Open Sans, Arial, sans-serif">
      <text x="6" y="11" font-size="4" font-weight="700" class="fi">Customer Email</text>
      <path d="M52 22a24 24 0 1 1-24 24" class="nf sa" stroke-width="2"/>
      <path d="M52 29a17 17 0 1 1-17 17" class="nf" style="stroke:var(--accent-mid)" stroke-width="2"/>
      <path d="M52 36a10 10 0 1 1-10 10" class="nf" style="stroke:var(--accent-dark)" stroke-width="1.5"/>
      <g font-size="3.2" class="fm"><circle cx="8" cy="84" r="1.5" class="fa"/><text x="11" y="85">12.5% Sent</text><circle cx="34" cy="84" r="1.5" class="fam"/><text x="37" y="85">25.2% Opened</text><circle cx="64" cy="84" r="1.5" class="fad"/><text x="67" y="85">50.6% Not Opened</text></g>
    </svg>
  </div>
  <div class="url">www.brellmoor.edu/english/</div><div class="page">Page | <b>14</b></div>
</section>

<!-- 15 Research Timeline area -->
<section class="slide col-l" style="top:2367px">
  <div class="eyebrow">Collage University</div><div class="title">Research Timeline</div>
  <div class="brand"><div class="brand-dot"></div><div class="brand-name">Brellmoor<br>University</div></div><div class="brand-rule"></div>
  <div class="abs tiny" style="left:34px;top:62px;width:150px">Lorem ipsum dolor sit amet, consectetur adipiscing elit. Maecenas porttitor congue massa. Fusce posuere, magna sed pulvinar ultricies, purus lectus malesuada libero, sit amet commodo magna eros quis urna.<br><br>Nunc viverra imperdiet enim. Fusce est. Vivamus a tellus. Pellentesque habitant morbi tristique senectus et netus et malesuada fames ac turpis egestas. Proin pharetra nonummy pede.</div>
  <div class="abs" style="left:210px;top:62px;display:flex;gap:6px"><span style="width:12px;height:12px;border-radius:50%;border:1px solid var(--accent)"></span><span class="tiny" style="border-left:1px solid var(--accent);padding-left:4px;width:140px">Lorem ipsum dolor sit amet, consectetur adipiscing elit. Maecenas porttitor congue massa.</span></div>
  <div class="abs" style="left:210px;top:84px;display:flex;gap:6px"><span style="width:12px;height:12px;border-radius:50%;border:1px solid var(--accent)"></span><span class="tiny" style="border-left:1px solid var(--accent);padding-left:4px;width:140px">Lorem ipsum dolor sit amet, consectetur adipiscing elit. Maecenas porttitor congue massa.</span></div>
  <div class="card darkcard center" style="left:32px;top:160px;width:56px;height:36px;padding-top:6px"><div style="font-size:12px">40K</div><div style="font-size:3.5px">Value One</div></div>
  <div class="card darkcard center" style="left:96px;top:160px;width:56px;height:36px;padding-top:6px"><div style="font-size:12px">60K</div><div style="font-size:3.5px">Value Two</div></div>
  <svg class="abs" style="left:0;top:0" width="464" height="261" font-family="Open Sans, Arial, sans-serif">
    <path d="M192 192c20-8 30-10 50-12s40-6 60-8 40-4 60-8 20-6 36-12v40h-206z" class="fa"/>
    <line x1="278" y1="178" x2="278" y2="160" class="sa" stroke-dasharray="2 2"/><rect x="266" y="150" width="24" height="9" class="fa"/><text x="278" y="156.5" font-size="4" class="fw" text-anchor="middle">40K</text>
    <line x1="356" y1="168" x2="356" y2="138" class="sa" stroke-dasharray="2 2"/><rect x="344" y="128" width="24" height="9" class="fw st"/><text x="356" y="134.5" font-size="4" class="fi" text-anchor="middle">60K</text>
    <circle cx="278" cy="178" r="2" class="fw sa"/>
    <g font-size="3.5" class="fm" text-anchor="middle"><text x="196" y="210">Jan</text><text x="217" y="210">Feb</text><text x="238" y="210">Mar</text><text x="259" y="210">Apr</text><text x="280" y="210">May</text><text x="301" y="210">Jun</text><text x="322" y="210">Jul</text><text x="343" y="210">Aug</text><text x="364" y="210">Sep</text><text x="385" y="210">Oct</text><text x="406" y="210">Nov</text><text x="427" y="210">Dec</text></g>
  </svg>
  <div class="url">www.brellmoor.edu/english/</div><div class="page">Page | <b>15</b></div>
</section>

<!-- 16 Research Timeline dark -->
<section class="slide dark col-r" style="top:2367px">
  <div class="eyebrow">Collage University</div><div class="title">Research Timeline</div>
  <div class="brand"><div class="brand-dot"></div><div class="brand-name">Brellmoor<br>University</div></div><div class="brand-rule"></div>
  <div class="abs" style="left:26px;top:64px;width:66px;height:60px;background:var(--accent-light);box-shadow:0 3px 8px rgba(0,0,0,.25)"></div>
  <div class="abs" style="left:106px;top:64px;width:66px;height:60px;background:rgba(0,0,0,.18)"></div>
  <div class="abs" style="left:26px;top:134px;width:66px;height:60px;background:rgba(0,0,0,.18)"></div>
  <div class="abs" style="left:106px;top:134px;width:66px;height:60px;background:rgba(0,0,0,.18)"></div>
  <svg class="abs" style="left:0;top:0" width="464" height="261" font-family="Open Sans, Arial, sans-serif">
    <g class="nf" style="stroke:rgba(255,255,255,.8)"><circle cx="59" cy="84" r="10"/><circle cx="139" cy="84" r="10"/><circle cx="59" cy="154" r="10"/><circle cx="139" cy="154" r="10"/></g>
    <g class="fw" font-size="5" text-anchor="middle"><text x="59" y="86">80%</text><text x="139" y="86">70%</text><text x="59" y="156">60%</text><text x="139" y="156">50%</text></g>
    <g class="fw" font-size="3" text-anchor="middle"><text x="59" y="106">Business Enhancement Plans</text><text x="59" y="111">Main Growth Strategy</text><text x="139" y="106">Business Enhancement Plans</text><text x="139" y="111">Main Growth Strategy</text><text x="59" y="176">Business Enhancement Plans</text><text x="59" y="181">Main Growth Strategy</text><text x="139" y="176">Business Enhancement Plans</text><text x="139" y="181">Main Growth Strategy</text></g>
    <rect x="184" y="64" width="254" height="130" style="fill:rgba(255,255,255,.05)"/>
    <text x="194" y="78" font-size="4.5" class="fw" font-weight="600">Profit Monitoring</text>
    <path d="M200 174c20 0 30-40 50-40s30 40 50 40 40-20 60-40 30 20 50 20v14h-210z" style="fill:rgba(255,255,255,.18)"/>
    <path d="M200 174c20 0 30-40 50-40s30 40 50 40 40-20 60-40 30 20 50 20" class="nf sw"/>
    <rect x="344" y="108" width="32" height="16" style="fill:rgba(255,255,255,.25)"/><text x="360" y="115" font-size="3.5" class="fw" text-anchor="middle">July</text><text x="360" y="121" font-size="4.5" class="fw" text-anchor="middle">10,000</text>
    <circle cx="359" cy="136" r="2" class="fw"/>
    <g font-size="3.5" class="fw" text-anchor="middle"><text x="202" y="186">Jan</text><text x="228" y="186">Feb</text><text x="254" y="186">Mar</text><text x="280" y="186">Apr</text><text x="306" y="186">May</text><text x="332" y="186">Jun</text><text x="358" y="186">Jul</text><text x="384" y="186">Aug</text><text x="410" y="186">Sep</text></g>
  </svg>
  <div class="url">www.brellmoor.edu/english/</div><div class="page">Page | <b>16</b></div>
</section>

<!-- 17 Research Timeline bars -->
<section class="slide col-l" style="top:2690px">
  <div class="eyebrow">Collage University</div><div class="title">Research Timeline</div>
  <div class="brand"><div class="brand-dot"></div><div class="brand-name">Brellmoor<br>University</div></div><div class="brand-rule"></div>
  <div class="photo" style="left:42px;top:56px;width:158px;height:160px;background:linear-gradient(160deg,#d8d8dc,#96969d)" role="img" aria-label="Portrait photo of a doctor with a stethoscope"></div>
  <svg class="abs" style="left:216px;top:60px" width="10" height="150"><line x1="5" y1="0" x2="5" y2="150" class="st"/></svg>
  <div class="abs" style="left:222px;top:66px;font-size:7px;font-weight:600">2023<div class="accent-text" style="font-size:3.5px;font-weight:400">60%</div></div>
  <div class="bar-track" style="left:248px;top:70px;width:170px"><div class="bar-fill" style="width:60%"></div></div>
  <div class="abs" style="left:222px;top:124px;font-size:7px;font-weight:600">2024<div class="accent-text" style="font-size:3.5px;font-weight:400">76%</div></div>
  <div class="bar-track" style="left:248px;top:128px;width:170px"><div class="bar-fill" style="width:73%"></div></div>
  <div class="abs" style="left:222px;top:182px;font-size:7px;font-weight:600">2025<div class="accent-text" style="font-size:3.5px;font-weight:400">84%</div></div>
  <div class="bar-track" style="left:248px;top:186px;width:170px"><div class="bar-fill" style="width:81%"></div></div>
  <div class="url">www.brellmoor.edu/english/</div><div class="page">Page | <b>17</b></div>
</section>

<!-- 18 Sunburst Chart -->
<section class="slide col-r" style="top:2690px">
  <div class="eyebrow">Collage University</div><div class="title">Sunburst Chart</div>
  <div class="brand"><div class="brand-dot"></div><div class="brand-name">Brellmoor<br>University</div></div><div class="brand-rule"></div>
  <svg class="abs" style="left:0;top:0" width="464" height="261" font-family="Open Sans, Arial, sans-serif">
    <circle cx="112" cy="128" r="42" class="ft"/>
    <path d="M112 86a42 42 0 0 1 30 72l-30-30z" class="fa"/>
    <path d="M142 158a42 42 0 0 1-58 0l28-30z" class="fal"/>
    <circle cx="112" cy="128" r="30" class="fts"/>
    <path d="M112 98a30 30 0 1 1-26 45l26-15z" class="fam"/>
    <circle cx="112" cy="128" r="22" class="fw"/>
    <circle cx="72" cy="196" r="2.5" class="fa"/><text x="78" y="198" font-size="5" class="fi">Role</text>
    <circle cx="140" cy="196" r="2.5" class="fam"/><text x="146" y="198" font-size="5" class="fi">User</text>
    <g font-size="8"><circle cx="246" cy="88" r="2.5" class="fad"/><text x="252" y="88" class="fad">38%</text><circle cx="246" cy="134" r="2.5" class="fa"/><text x="252" y="134" class="fa">33%</text><circle cx="246" cy="180" r="2.5" class="fal"/><text x="252" y="180" class="fal">29%</text></g>
    <g font-size="8"><circle cx="350" cy="88" r="2.5" class="fal"/><text x="356" y="88" class="fal">40%</text><circle cx="350" cy="134" r="2.5" class="fam"/><text x="356" y="134" class="fam">30%</text><circle cx="350" cy="180" r="2.5" style="fill:#b0b0b6"/><text x="356" y="180" style="fill:#b0b0b6">30%</text></g>
    <g font-size="4" class="fm"><text x="252" y="96">August 2022</text><text x="252" y="142">September 2022</text><text x="252" y="188">October 2022</text><text x="356" y="96">August 2022</text><text x="356" y="142">September 2022</text><text x="356" y="188">October 2022</text></g>
  </svg>
  <div class="url">www.brellmoor.edu/english/</div><div class="page">Page | <b>18</b></div>
</section>

<!-- 19 Research Timeline stats -->
<section class="slide col-l" style="top:3012px">
  <div class="eyebrow">Collage University</div><div class="title">Research Timeline</div>
  <div class="brand"><div class="brand-dot"></div><div class="brand-name">Brellmoor<br>University</div></div><div class="brand-rule"></div>
  <div class="card" style="left:54px;top:96px;width:86px;height:68px;padding:26px 0 0 20px"><div class="accent-text" style="font-size:11px">56bn</div><div class="tiny">August 2023</div></div>
  <svg class="abs" style="left:112px;top:104px" width="18" height="18"><circle cx="9" cy="9" r="7" class="nf sa" stroke-dasharray="3 2"/><circle cx="9" cy="9" r="3" class="nf sa"/></svg>
  <div class="card darkcard" style="left:188px;top:92px;width:86px;height:70px;padding:26px 0 0 16px"><div style="font-size:11px">6mn</div><div class="tiny" style="color:#fff">September 2023</div></div>
  <svg class="abs" style="left:246px;top:100px" width="20" height="20"><rect x="2" y="9" width="7" height="7" class="nf sw"/><rect x="11" y="9" width="7" height="7" class="nf sw"/><rect x="6" y="2" width="7" height="7" class="nf sw"/></svg>
  <div class="card" style="left:320px;top:96px;width:86px;height:68px;padding:26px 0 0 20px"><div class="accent-text" style="font-size:11px">8um</div><div class="tiny">October 2023</div></div>
  <svg class="abs" style="left:378px;top:104px" width="18" height="18"><circle cx="9" cy="10" r="6" class="nf sa"/><circle cx="9" cy="10" r="2.5" class="nf sa"/><line x1="9" y1="1" x2="9" y2="4" class="sa"/></svg>
  <div class="url">www.brellmoor.edu/english/</div><div class="page">Page | <b>19</b></div>
</section>

<!-- 20 Thank You -->
<section class="slide dark col-r" style="top:3012px">
  <div class="abs center" style="left:0;width:464px;top:90px;font-size:22px;font-weight:700">Thank You</div>
  <div class="abs" style="left:136px;top:126px;width:192px;height:1px;background:rgba(255,255,255,.7)"></div>
  <div class="abs center" style="left:132px;top:136px;width:200px;font-size:4px;line-height:1.6">Lorem ipsum dolor sit amet, consectetur adipiscing elit. Maecenas porttitor congue massa. Fusce posuere, magna sed pulvinar ultricies, purus lectus malesuada libero, sit amet commodo magna eros quis urna.</div>
</section>

</body>
</html>
```